Maple Crest Tutoring General Flyer Design

Reason: We are very close to making a selection but would like to provide a little more time for some of the designers to complete their revisions.
Target Market(s)
Secondary school students
Industry/Entity Type
Education
Requirements
Must have
- company logo and company name (see attached file)

```html
<!DOCTYPE html>
<html lang="en">
<head>
<meta charset="utf-8">
<title>Maple Crest Tutoring – Math Flyer</title>
<link rel="stylesheet" href="https://fonts.googleapis.com/css2?family=Arimo:ital,wght@0,400;0,700;1,400;1,700&display=swap">
<style>
  :root {
    --red-deep: #8e0f14;
    --red: #c8161d;
    --red-bright: #e01f26;
    --cream: #fbeec6;
    --cream-light: #fdf6de;
    --gold: #f7c96a;
    --gold-light: #fde7a8;
    --ink: #1a1a1a;
    --white: #ffffff;
    --promo-yellow: #ffd84a;
  }
  * { box-sizing: border-box; margin: 0; padding: 0; }
  html, body { width: 776px; height: 1200px; overflow: hidden; background: var(--white); }
  body { font-family: "Arimo", Arial, sans-serif; color: var(--ink); }

  .flyer { position: relative; width: 776px; height: 1200px; overflow: hidden; }

  .title-band {
    position: absolute; left: 0; top: 0; width: 776px; height: 122px;
    background: linear-gradient(90deg, var(--red-bright) 0%, var(--red) 50%, var(--red-deep) 100%);
    display: flex; align-items: center; justify-content: center;
  }
  .title-band h1 {
    color: var(--white); font-weight: 700; font-size: 84px; letter-spacing: 30px;
    margin-right: -30px; line-height: 1;
  }

  .subtitle-band {
    position: absolute; left: 0; top: 122px; width: 776px; height: 110px;
    background: linear-gradient(180deg, var(--cream-light), var(--cream));
    text-align: center; color: var(--red-deep); font-weight: 700;
  }
  .subtitle-band .from { font-size: 38px; line-height: 1; padding-top: 14px; }
  .subtitle-band .headline { font-size: 40px; line-height: 1.1; margin-top: 4px; }

  .hero {
    position: absolute; left: 0; top: 232px; width: 776px; height: 454px;
    background: linear-gradient(180deg, #5f6a62 0%, #7a857c 45%, #9aa39b 100%);
  }
  .hero-caption {
    position: absolute; left: 0; top: 610px; width: 776px; height: 70px;
    display: flex; align-items: center; justify-content: center;
    background: linear-gradient(180deg, rgba(255,255,255,0) 0%, rgba(255,255,255,0.55) 40%, rgba(255,255,255,0.75) 100%);
    font-weight: 700; font-size: 36px; color: #000;
  }
  .divider { position: absolute; left: 0; top: 680px; width: 776px; height: 8px; background: var(--red); }

  .brand-panel {
    position: absolute; left: 0; top: 688px; width: 353px; height: 232px;
    background: linear-gradient(180deg, var(--gold) 0%, var(--gold-light) 100%);
    display: flex; flex-direction: column; align-items: center; justify-content: center; text-align: center;
  }
  .brand-mark { width: 70px; height: 70px; border-radius: 50%; background: var(--red-deep); margin-bottom: 18px; }
  .brand-name { font-weight: 700; font-size: 29px; color: var(--ink); }
  .tagline { font-style: italic; color: var(--red); font-size: 25px; line-height: 1.15; margin-top: 6px; }

  .courses {
    position: absolute; left: 353px; top: 688px; width: 423px; height: 232px;
    background: var(--white); padding: 30px 28px 0 40px;
  }
  .courses h2 { font-style: italic; font-weight: 400; color: var(--red); font-size: 25px; margin-bottom: 14px; }
  .courses ol { list-style: none; font-size: 19px; line-height: 1.25; }
  .courses li { margin-bottom: 8px; }

  .contact {
    position: absolute; left: 0; top: 920px; width: 353px; height: 280px;
    background: linear-gradient(180deg, #fbe2a4 0%, var(--cream-light) 100%);
  }
  .map {
    position: absolute; left: 36px; top: 40px; width: 104px; height: 86px;
    background: linear-gradient(135deg, #e6ebe2, #cdd8c8);
  }
  .address { position: absolute; left: 156px; top: 36px; font-size: 17px; line-height: 1.4; }
  .phone { position: absolute; left: 156px; top: 124px; font-size: 25px; font-weight: 700; color: var(--red); }
  .contact-rule { position: absolute; left: 28px; top: 176px; width: 298px; height: 2px; background: var(--red); }
  .web { position: absolute; left: 0; top: 200px; width: 353px; text-align: center; font-size: 16px; line-height: 1.55; }

  .promo {
    position: absolute; left: 353px; top: 920px; width: 423px; height: 280px;
    background: linear-gradient(135deg, var(--red-bright) 0%, var(--red) 45%, var(--red-deep) 100%);
    text-align: center; padding-top: 30px; font-style: italic;
  }
  .promo .label { color: var(--promo-yellow); font-size: 22px; }
  .promo .offer { color: var(--white); font-size: 28px; margin-top: 8px; }
  .promo .cta { color: var(--promo-yellow); font-size: 28px; margin-top: 6px; }
  .promo .note { color: var(--white); font-size: 22px; line-height: 1.35; margin-top: 6px; }
</style>
</head>
<body>
  <main class="flyer">
    <header class="title-band"><h1>MATH</h1></header>

    <section class="subtitle-band">
      <p class="from">from</p>
      <p class="headline">Abstract to Concrete</p>
    </section>

    <div class="hero" role="img" aria-label="Photo of a student seen from behind, scratching his head in front of a chalkboard full of equations"></div>
    <p class="hero-caption">We can help make the connection</p>
    <div class="divider"></div>

    <section class="brand-panel">
      <div class="brand-mark"></div>
      <p class="brand-name">Maple Crest Tutoring</p>
      <p class="tagline">Your Pathway<br>to Excellence</p>
    </section>

    <section class="courses">
      <h2>MATH WE TUTOR:</h2>
      <ol>
        <li>1) Ontario Math G.9 – 12</li>
        <li>2) IB Math High Level , Standard<br>&nbsp;&nbsp;&nbsp;&nbsp;Level, Math Studies</li>
        <li>3) AP Calculus AB/BC</li>
        <li>4) University Year 1 Calculus</li>
      </ol>
    </section>

    <section class="contact">
      <div class="map" role="img" aria-label="Small street map showing the tutoring centre location"></div>
      <p class="address">4120 Birchwood Avenue,<br>Unit 305<br>Markham, ON L3R 2K9</p>
      <p class="phone">647-555-0148</p>
      <div class="contact-rule"></div>
      <p class="web">www.MapleCrestTutoring.com<br>Service@MapleCrestTutoring.com</p>
    </section>

    <section class="promo">
      <p class="label">PROMOTIONAL OFFER:</p>
      <p class="offer">FREE TRIAL LESSON</p>
      <p class="cta">CALL OR EMAIL</p>
      <p class="note">US TODAY<br>FOR A FREE TRIAL LESSON!</p>
    </section>
  </main>
</body>
</html>
```